Wine Label front and back- Need to have an eye catching, classy wine label for restaurant placement.

label design for a wine label. eye catching for shelf placement. looking for simple and elegant label. Name of the vineyard will be the label recognition. Need back label to match with coloring and basic regulated info required by gov't (producer, address, and statement) Back label will be addressed after selected front label to match.
Will add $100 extra for the back label to match.

Target Market(s)

40-65 year old foodies

Colors
0355a3
eaf1f7

Requirements
Must have
• FERNHOLLOW (label name)
Estate,
Red Wine Blend NV,

```html
<!DOCTYPE html>
<html lang="en">
<head>
<meta charset="utf-8">
<title>Fernhollow Estate – Red Wine Blend NV</title>
<link rel="stylesheet" href="https://fonts.googleapis.com/css2?family=Playball&family=Montserrat:wght@600;700&family=Crimson+Text&display=swap">
<style>
  :root {
    --brand-blue: #0355a3;
    --label-mist: #eaf1f7;
    --label-face: #f2f6fa;
    --copper: #b97a45;
    --wheat: #c98f5c;
    --ink: #333333;
    --paper: #ffffff;
  }
  * { margin: 0; padding: 0; box-sizing: border-box; }
  html, body { width: 1200px; height: 1200px; overflow: hidden; background: var(--paper); }
  .canvas { position: relative; width: 1200px; height: 1200px; background: var(--paper); }
  .label-art { position: absolute; inset: 0; }
  .label-text { position: absolute; left: 0; width: 1200px; text-align: center; }
  .established {
    top: 356px; font-family: "Montserrat", sans-serif; font-weight: 700;
    font-size: 22px; letter-spacing: 4px; color: var(--ink);
  }
  .estate-name {
    top: 488px; font-family: "Playball", cursive; font-size: 118px;
    line-height: 1.2; color: var(--brand-blue);
  }
  .estate-word {
    top: 680px; font-family: "Montserrat", sans-serif; font-weight: 700;
    font-size: 22px; letter-spacing: 2px; color: var(--ink);
  }
  .wine-type {
    top: 756px; font-family: "Crimson Text", serif; font-size: 36px; color: var(--ink);
  }
</style>
</head>
<body>
<main class="canvas">
  <svg class="label-art" width="1200" height="1200" viewBox="0 0 1200 1200" xmlns="http://www.w3.org/2000/svg">
    <defs>
      <path id="label-outline" d="M312,378 L440,378 C480,338 540,316 600,316 C660,316 720,338 760,378 L888,378 L888,420 C888,480 920,520 950,520 C1010,520 1040,560 1040,604 C1040,648 1010,688 950,688 C920,688 888,728 888,788 L888,830 L760,830 C720,870 660,893 600,893 C540,893 480,870 440,830 L312,830 L312,788 C312,728 280,688 250,688 C190,688 160,648 160,604 C160,560 190,520 250,520 C280,520 312,480 312,420 Z"/>
      <linearGradient id="wheat-tone" x1="0" y1="0" x2="0" y2="1">
        <stop offset="0" stop-color="var(--wheat)" stop-opacity="0.55"/>
        <stop offset="1" stop-color="var(--wheat)" stop-opacity="0.25"/>
      </linearGradient>
    </defs>
    <rect class="brand-band" x="0" y="407" width="1200" height="386" fill="var(--brand-blue)"/>
    <use class="label-halo" href="#label-outline" fill="var(--label-mist)" stroke="var(--label-mist)" stroke-width="62" stroke-linejoin="round"/>
    <use class="label-face" href="#label-outline" fill="var(--label-face)"/>
    <use class="frame-outer" href="#label-outline" fill="none" stroke="var(--copper)" stroke-width="5"/>
    <use class="frame-inner" href="#label-outline" fill="none" stroke="var(--copper)" stroke-width="2" transform="translate(600 604) scale(0.975 0.965) translate(-600 -604)"/>
    <rect class="wheat-ornament" role="img" aria-label="Pair of crossed wheat sprigs ornament" x="428" y="402" width="344" height="82" rx="40" fill="url(#wheat-tone)"/>
    <line class="divider" x1="420" y1="735" x2="780" y2="735" stroke="var(--copper)" stroke-width="2"/>
  </svg>
  <p class="label-text established">EST 2021</p>
  <h1 class="label-text estate-name">Fernhollow</h1>
  <p class="label-text estate-word">ESTATE</p>
  <p class="label-text wine-type">Red Wine Blend NV</p>
</main>
</body>
</html>
```